" MINHA EMPRESA É PRESTADORA DE SERVIÇOS PARA ORGÃOS PUBLICOS, TRABALHAMOS EM VARIOS SEGMENTOS, SERVIÇOS DE REFORMA EM GERAL, FORNECIMENTO DE MATERIAL DE CONSTRUÇÃO, REALIZAÇÃO DE EVENTOS, DETRE VARIOS OUTROS MAIS. "

```html
<!DOCTYPE html>
<html lang="pt-BR">
<head>
<meta charset="utf-8">
<title>Valterra — Pasta institucional</title>
<link rel="stylesheet" href="https://fonts.googleapis.com/css2?family=Michroma&family=Exo+2:wght@500;600&display=swap">
<style>
  :root {
    --navy: #1c2b4c;
    --teal: #2ba4ad;
    --teal-dark: #1f8a93;
    --white: #ffffff;
    --backdrop: #e9e6e1;
    --ghost: #eef0f3;
    --muted: #c9d3e2;
  }
  * { box-sizing: border-box; margin: 0; padding: 0; }
  html, body { width: 1200px; height: 1200px; overflow: hidden; }
  body { background: var(--backdrop); position: relative; font-family: "Exo 2", sans-serif; }

  .folder {
    position: absolute; left: 60px; top: 252px;
    width: 1032px; height: 756px;
    display: flex;
    box-shadow: 0 14px 40px rgba(0,0,0,0.22);
  }
  .panel { position: relative; width: 516px; height: 100%; overflow: hidden; }
  .panel--back { background: var(--navy); }
  .panel--front { background: var(--white); }

  .flap { position: absolute; left: 0; top: 0; width: 516px; height: 84px; }

  .brand { position: absolute; left: 0; width: 100%; text-align: center; }
  .brand__name {
    font-family: "Michroma", sans-serif;
    font-size: 32px; letter-spacing: 1px; line-height: 1;
    display: inline-flex; align-items: center; gap: 12px;
  }
  .brand__dot { width: 14px; height: 14px; background: var(--teal); display: inline-block; }
  .brand__tagline {
    margin-top: 12px;
    font-family: "Exo 2", sans-serif; font-weight: 600;
    font-size: 15px; letter-spacing: 5px; color: var(--teal);
  }
  .panel--back .brand { top: 372px; }
  .panel--back .brand__name { color: var(--white); }
  .panel--front .brand { top: 240px; }
  .panel--front .brand__name { color: var(--navy); }

  .contact {
    position: absolute; left: 0; bottom: 50px; width: 100%;
    text-align: center; color: var(--muted);
    font-size: 9px; line-height: 12px; font-weight: 500;
  }
  .contact .web { color: var(--teal); }

  .ghost-name {
    position: absolute; left: 0; top: 590px; width: 100%;
    text-align: center;
    font-family: "Michroma", sans-serif;
    font-size: 52px; color: var(--ghost); line-height: 1;
  }

  .rule { position: absolute; left: 0; width: 100%; }
  .rule--top { top: 0; height: 6px; background: var(--teal); }
  .rule--thin { bottom: 30px; height: 4px; background: var(--teal); }
  .rule--thick { bottom: 0; height: 22px; background: var(--teal-dark); }
  .panel--front .rule--thin { bottom: 28px; height: 3px; }
  .panel--front .rule--thick { background: var(--teal); height: 18px; }
</style>
</head>
<body>
  <main class="folder">
    <section class="panel panel--back">
      <svg class="flap" viewBox="0 0 516 84" aria-hidden="true">
        <polygon points="0,0 516,0 516,20 470,84 0,84" fill="var(--teal)"/>
        <polygon points="470,84 516,20 516,84" fill="var(--navy)"/>
      </svg>
      <div class="brand">
        <div class="brand__name"><span class="brand__dot"></span>VALTERRA</div>
        <div class="brand__tagline">COMÉRCIO E SERVIÇOS</div>
      </div>
      <div class="contact">
        <div class="web">www.valterra.com.br</div>
        <div>Rua das Obras, 120 Centro - Cidade - UF - CEP 00.000-000</div>
        <div>(11) 5555-0100</div>
        <div>contato@valterra.com.br</div>
      </div>
      <div class="rule rule--thin"></div>
      <div class="rule rule--thick"></div>
    </section>

    <section class="panel panel--front">
      <div class="rule rule--top"></div>
      <div class="brand">
        <div class="brand__name"><span class="brand__dot"></span>VALTERRA</div>
        <div class="brand__tagline">COMÉRCIO E SERVIÇOS</div>
      </div>
      <div class="ghost-name" aria-hidden="true">VALTERRA</div>
      <div class="rule rule--thin"></div>
      <div class="rule rule--thick"></div>
    </section>
  </main>
</body>
</html>
```